"Tova's" Website Design

Tova's makes earth friendly, healthy, and delicious snacks that are completely gluten free. We are looking for a website that is easy to navigate, energetic, and conveys our purpose "To create healthy, earth-friendly, gluten free snacks that fill bellies and warm hearts."
Our first product is "Tova's Cheese Bursts" are a small, square, cracker pack with an unreasonable amount of cheddar cheese flavor. The flavor literally explodes in your mouth!
We really want our site to pop and show off some personality.
I'm attaching the logo for the company, feel free to go beyond the logo in terms of color.
Here are some sites that we like!
http://www.pollwinkle.example/company
http://www.brenmoor.example/
http://www.qx47.example/
http://www.teddyvales.example/
http://www.dunrise.example/food/products_zest/
http://www.marvelfrost.example/

```html
<!DOCTYPE html>
<html lang="en">
<head>
<meta charset="utf-8">
<title>Tova's</title>
<link rel="stylesheet" href="https://fonts.googleapis.com/css2?family=Amaranth:wght@400;700&family=Crimson+Text:ital@0;1&display=swap">
<style>
:root{
  --orange:#f26522;
  --blue:#336a94;
  --blue-dark:#23506f;
  --tan-light:#f1ead9;
  --tan:#cdb98f;
  --band:#5b5448;
  --ink:#2b2b2b;
  --social:#222222;
  --white:#ffffff;
}
*{box-sizing:border-box;margin:0;padding:0}
html,body{width:950px;height:1200px;overflow:hidden}
body{font-family:Arial,Helvetica,sans-serif;color:var(--ink);background:var(--tan)}
.page{position:relative;width:950px;height:1200px;overflow:hidden;
  background:
    radial-gradient(ellipse 520px 300px at 475px 230px,var(--tan-light),rgba(241,234,217,0) 100%),
    linear-gradient(180deg,#c9b68e 0,#d6c59f 300px,#c4b089 900px);}
.lower{position:absolute;left:0;top:900px;width:950px;height:210px;
  background:linear-gradient(180deg,#fafafa 0,#e4e4e4 60px,#8a8a8a 160px,#555 210px)}
.abs{position:absolute}

/* nav */
.nav-line{position:absolute;height:3px;background:var(--orange);top:37px}
.nav-dot{position:absolute;width:10px;height:10px;border-radius:50%;background:#111;top:38px}
.nav-btn{position:absolute;top:18px;height:53px;width:91px;border:1px solid #fff;
  font-family:"Amaranth",sans-serif;font-size:21px;color:var(--white);text-align:center;line-height:50px;white-space:nowrap;
  background:linear-gradient(180deg,#5a8cb4,#2f5f85);box-shadow:0 3px 5px rgba(0,0,0,.35);text-decoration:none}
.nav-btn.is-active{background:linear-gradient(180deg,#ffffff,#d9d9d9);color:#111;border-color:#555}
.nav-active-bar{position:absolute;left:362px;top:71px;width:91px;height:9px;background:var(--orange)}

.brand{position:absolute;left:40px;top:78px;font-family:"Amaranth",sans-serif;font-size:84px;color:var(--orange);line-height:1}

.find{position:absolute;font-weight:bold;font-size:12px;color:#111;letter-spacing:-.4px;white-space:nowrap;text-align:right}
.social{position:absolute;width:31px;height:31px;border-radius:6px;background:var(--social);border:2px solid #fff;
  box-shadow:0 2px 3px rgba(0,0,0,.5);font-size:9px;color:#fff;text-align:center;line-height:27px}

.search{position:absolute;left:768px;top:170px;width:171px;height:17px;display:flex;box-shadow:0 4px 6px rgba(0,0,0,.3)}
.search-field{flex:1;background:#fff;border:1px solid var(--blue);font:italic 9px "Crimson Text",serif;color:var(--blue);padding:2px 10px}
.search-btn{width:25px;background:var(--orange)}

/* carousel */
.slide{position:absolute;box-shadow:0 4px 10px rgba(0,0,0,.35);border:1px solid #666}
.dots{position:absolute;display:flex;gap:4px}
.dots span{width:10px;height:10px;border-radius:50%;background:var(--blue)}
.dots span.on{background:var(--orange);border:1px solid #fff}
.slide-title{position:absolute;width:226px;text-align:center;font-family:"Amaranth",sans-serif;font-weight:700;font-size:13px;color:#fff;text-shadow:0 1px 2px #000}
.slide-text{position:absolute;width:200px;font-size:8px;font-style:italic;line-height:10px;color:#222}
.arrow{position:absolute;width:24px;height:28px}

/* band */
.band{position:absolute;left:0;top:545px;width:950px;height:155px;background:linear-gradient(180deg,rgba(80,72,58,.85),rgba(95,86,70,.9))}
.band-title{position:absolute;left:240px;top:550px;font-family:"Amaranth",sans-serif;font-weight:700;font-size:30px;color:#fff}
.band-quote{position:absolute;left:120px;top:598px;width:730px;font-size:14px;font-style:italic;line-height:17px;color:#fff}
.band-more{position:absolute;left:792px;top:675px;font-size:14px;color:#fff;text-decoration:underline}
.rule{position:absolute;left:15px;top:698px;width:917px;border-top:1px dashed #eee}

/* features */
.feature-bar{position:absolute;top:715px;width:282px;height:34px;border:1px solid #fff;background:linear-gradient(180deg,#5c8db4,#2f5f85);box-shadow:0 2px 4px rgba(0,0,0,.35)}
.feature-bar .tab{position:absolute;left:0;top:0;width:15px;height:32px;background:var(--orange)}
.feature-bar h2{position:absolute;left:17px;top:1px;font-family:"Amaranth",sans-serif;font-weight:400;font-size:22px;color:#fff;white-space:nowrap}
.feature-bar .dot{position:absolute;left:164px;top:13px;width:8px;height:8px;border-radius:50%;background:#fff}
.feature-bar .streak{position:absolute;left:172px;top:16px;width:108px;height:3px;background:var(--orange)}
.feature-photo{position:absolute;top:751px;width:282px;height:201px;box-shadow:0 5px 8px rgba(0,0,0,.35)}
.feature-text{position:absolute;top:967px;font-size:11px;line-height:13.5px;color:#222;white-space:nowrap}
.more{position:absolute;font:italic 12px "Crimson Text",serif;color:var(--orange);text-decoration:underline;white-space:nowrap}
.divider{position:absolute;top:930px;width:1px;height:160px;background:#aaa}

/* footer */
.footer{position:absolute;left:0;top:1110px;width:950px;height:90px;background:var(--blue)}
.footer-links{position:absolute;left:28px;top:1122px;font:italic 13px "Crimson Text",serif;color:#fff}
.footer-note{position:absolute;left:20px;top:1156px;font-size:7.5px;font-style:italic;line-height:9.5px;color:#fff;white-space:nowrap}
.copyright{position:absolute;left:390px;top:1179px;font:11px "Crimson Text",serif;color:#fff}
</style>
</head>
<body>
<div class="page">
  <div class="lower"></div>

  <!-- navigation -->
  <div class="nav-line" style="left:0;width:325px"></div>
  <div class="nav-dot" style="left:324px"></div>
  <svg class="abs" style="left:339px;top:28px" width="22" height="20" viewBox="0 0 22 20" aria-label="Home">
    <path d="M11 1 1 10h3v9h5v-6h4v6h5v-9h3z" fill="#111"/>
  </svg>
  <a class="nav-btn is-active" style="left:362px">Home</a>
  <div class="nav-active-bar"></div>
  <a class="nav-btn" style="left:502px">Products</a>
  <a class="nav-btn" style="left:644px">About us</a>
  <a class="nav-btn" style="left:784px">Contact</a>
  <div class="nav-dot" style="left:877px"></div>
  <div class="nav-line" style="left:886px;width:64px;top:42px"></div>

  <div class="brand">Tova's</div>

  <div class="find" style="right:162px;top:126px">Find us on:</div>
  <div class="social" style="left:795px;top:117px">Pix</div>
  <div class="social" style="left:833px;top:117px">Buzz</div>
  <div class="social" style="left:871px;top:117px">Orb</div>
  <div class="social" style="left:908px;top:117px">Net</div>

  <div class="search">
    <div class="search-field">Search on Tova's</div>
    <div class="search-btn">
      <svg width="25" height="17" viewBox="0 0 25 17" aria-label="Search">
        <circle cx="11" cy="7" r="4.5" fill="none" stroke="#111" stroke-width="2"/>
        <path d="M14 10l5 5" stroke="#111" stroke-width="2.5"/>
      </svg>
    </div>
  </div>

  <!-- carousel -->
  <div class="slide" role="img" aria-label="Golden cheese bursts frying in a basket" style="left:122px;top:277px;width:227px;height:145px;background:linear-gradient(160deg,#b8b6b0,#8a7350 55%,#d79a3c)"></div>
  <div class="dots" style="left:287px;top:279px"><span></span><span></span><span></span><span class="on"></span></div>
  <div class="slide-title" style="left:122px;top:423px">Lorem Ipsum</div>
  <div class="slide-text" style="left:130px;top:438px">“ is simply dummy text of the printing and typesetting industry. Lorem Ipsum has been the industry's standard dummy text ever since the 1500s, when an unknown printer took a galley of type and scrambled ”</div>
  <svg class="arrow" style="left:291px;top:482px" viewBox="0 0 24 28" aria-label="Previous"><circle cx="12" cy="12" r="11" fill="#ddd" stroke="#333" stroke-width="2"/><path d="M15 12H7m4-4-4 4 4 4" stroke="#222" stroke-width="2.5" fill="none"/></svg>

  <div class="slide" role="img" aria-label="Plated roast dish on a restaurant table" style="left:385px;top:254px;width:183px;height:60px;background:linear-gradient(90deg,#c23b2a,#d9cfc2 40%,#8a4a22)"></div>
  <div class="dots" style="left:518px;top:256px"><span></span><span></span><span class="on"></span><span></span></div>

  <div class="slide" role="img" aria-label="Tray of fried cheese bursts at a market stall" style="left:605px;top:276px;width:227px;height:145px;background:linear-gradient(160deg,#f0e3c0,#e8c35a 45%,#7a5f3a)"></div>
  <div class="dots" style="left:770px;top:279px"><span></span><span class="on"></span><span></span><span></span></div>
  <div class="slide-title" style="left:620px;top:421px">Lorem Ipsum</div>
  <div class="slide-text" style="left:631px;top:438px">“ is simply dummy text of the printing and typesetting industry. Lorem Ipsum has been the industry's standard dummy text ever since the 1500s, when an unknown printer took a galley of type and scrambled ”</div>
  <svg class="arrow" style="left:636px;top:482px" viewBox="0 0 24 28" aria-label="Next"><circle cx="12" cy="12" r="11" fill="#ddd" stroke="#333" stroke-width="2"/><path d="M9 12h8m-4-4 4 4-4 4" stroke="#222" stroke-width="2.5" fill="none"/></svg>

  <div class="slide" role="img" aria-label="Bowl of crispy cheese bursts with serving tongs" style="left:335px;top:312px;width:283px;height:203px;background:linear-gradient(150deg,#e8902a 0,#c98a45 35%,#8a6a3e 70%,#555 100%);box-shadow:0 18px 18px -8px rgba(0,0,0,.45)"></div>
  <div class="dots" style="left:543px;top:314px"><span class="on"></span><span></span><span></span><span></span></div>

  <!-- statement band -->
  <div class="band"></div>
  <div class="band-title">Lorem Ipsum</div>
  <p class="band-quote">“ is simply dummy text of the printing and typesetting industry. Lorem Ipsum has been the industry's standard dummy text ever since the 1500s, when an unknown printer took a galley of type and scrambled it to make a type specimen book. It has survived not only five centuries, but also the leap into electronic typesetting, remaining essentially unchanged. It was popularised in the 1960s with the release of Lettrix sheets containing Lorem Ipsum passages ”</p>
  <a class="band-more">Read more --&gt;</a>
  <div class="rule"></div>

  <!-- features -->
  <div class="feature-bar" style="left:15px"><div class="tab"></div><h2>About us</h2><div class="dot"></div><div class="streak"></div></div>
  <div class="feature-photo" role="img" aria-label="Snack ingredients laid out on a wooden board" style="left:15px;background:linear-gradient(170deg,#c8c4bc,#b48a5a 50%,#6e5030)"></div>
  <p class="feature-text" style="left:31px">is simply dummy text of the printing and typesetting<br>industry. Lorem Ipsum has been the industry's stan-<br>dard dummy text ever since the 1500s, when an<br>unknown printer took a galley of type and scrambled<br>it to make a type specimen book. It has survived not<br>only five centuries, but also the leap into electronic<br>typesetting,</p>
  <a class="more" style="left:97px;top:1052px">Read more --&gt;</a>
  <div class="divider" style="left:316px"></div>

  <div class="feature-bar" style="left:333px"><div class="tab"></div><h2>Our Products</h2><div class="dot"></div><div class="streak"></div></div>
  <div class="feature-photo" role="img" aria-label="Cheese bursts served on a leaf plate" style="left:333px;background:linear-gradient(170deg,#2a2420,#7a6a48 45%,#e0d8c8)"></div>
  <p class="feature-text" style="left:341px">is simply dummy text of the printing and typesetting<br>industry. Lorem Ipsum has been the industry's standard<br>dummy text ever since the 1500s, when an unknown<br>printer took a galley of type and scrambled it to make a<br>type specimen book. It has survived not only five centu-<br>ries, but also the leap into electronic typesetting,</p>
  <a class="more" style="left:554px;top:1047px">Read more --&gt;</a>
  <div class="divider" style="left:633px"></div>

  <div class="feature-bar" style="left:651px"><div class="tab"></div><h2>Tova's Brand</h2><div class="dot"></div><div class="streak"></div></div>
  <div class="feature-photo" role="img" aria-label="Toasted cheese sandwich close-up" style="left:651px;background:linear-gradient(160deg,#3a2a18,#b97a3a 45%,#e9c9a0)"></div>
  <p class="feature-text" style="left:668px">is simply dummy text of the printing and typesetting<br>industry. Lorem Ipsum has been the industry's<br>standard dummy text ever since the 1500s, when an<br>unknown printer took a galley of type and scrambled<br>it to make a type specimen book. It has survived not<br>only five centuries, but also the leap into electronic<br>typesetting,</p>
  <a class="more" style="left:743px;top:1053px">Read more --&gt;</a>

  <!-- footer -->
  <div class="footer"></div>
  <nav class="footer-links">Home | Products | About us | Contact</nav>
  <p class="footer-note">is simply dummy text of the printing and typesetting industry. Lorem Ipsum has been the<br>industry's standard dummy text ever since the 1500s, when an unknown printer took a galley of<br>type and scrambl</p>
  <div class="copyright">Copyright 2012-to-2013 All rights reserved</div>
  <div class="find" style="right:164px;top:1169px;color:#fff">Find us on:</div>
  <div class="social" style="left:793px;top:1160px">Pix</div>
  <div class="social" style="left:831px;top:1160px">Buzz</div>
  <div class="social" style="left:868px;top:1160px">Orb</div>
  <div class="social" style="left:905px;top:1160px">Net</div>
</div>
</body>
</html>
```